Vocational Mentor needs an impressive business card

1. I need a business card (or maybe three with identic look) to promote me and my three business titles/services:
- Vocational Mentor. I help people find their vocation and live happily from it. I use my 20 years of experience in business, management and psychology to help them identify the most efficient ways to make a living doing what they are passionate about.
- Business Angel. I help founders start a succesful business with minimum risks and costs. I use my 20 years of experience in sales, management and entrepreneurship to help them identify the most efficient ways, in terms of time and cost, to validate their business idea.
- Learning Designer. I design unique learning programs that produce long-term cognitive and behavioural changes to people and organisations. I use my 20 years of experience in learning, teaching and change management to create minimalist experiences and processes that allow them to change efficiently in their pursued direction.

2. I would like a two-sided business card, on the front with my name, contact details and titles, on the back the explanation of the services.
Updates

Hi all,

I updated my brief, included contacts info and give feedback on all designs I got. I am new on this platform so please tell me if you need anything else or if I don't use corectly the platform forms.

Kind regards,
Tudor

Hi all,

I shortened the services description by deleting the phrase "I call..."

Kind regards,
Tudor

Target Market(s)

Freelancers, startups, people and organization willing to invest in change through ultimate learning experiences

Industry/Entity Type

Business

Font styles to use
Serif

Requirements
Must have
• Front side: full name, titles, web site, email, phone like below:
Tudor Vasilache
Vocational Mentor, Business Angel, Learning Designer
info@tudorvasilache.example
www.tudorvasilache.example
+40-745-TUDORV
Nice to have
• Back side: the description of the services I provide as in the task description.
1/3: it would be nice if I can jam all three titles on the front side but then I need a solution to jam all three services on the back side.

```html
<!DOCTYPE html>
<html lang="en">
<head>
<meta charset="utf-8">
<title>Tudor Vasilache – Business Card</title>
<link rel="stylesheet" href="https://fonts.googleapis.com/css2?family=Vollkorn:wght@400;600;700&display=swap">
<style>
  :root {
    --page-bg: #d9d4cc;
    --card-dark: #1c1c1c;
    --card-light: #fbfbfa;
    --gold: #b8994a;
    --text-light: #f4f2ee;
    --text-dark: #2a2a2a;
  }
  * { margin: 0; padding: 0; box-sizing: border-box; }
  html, body {
    width: 1200px;
    height: 1023px;
    overflow: hidden;
    background: var(--page-bg);
    font-family: "Vollkorn", Georgia, serif;
  }
  .canvas {
    position: relative;
    width: 1200px;
    height: 1023px;
    display: flex;
    align-items: center;
    justify-content: center;
  }
  .business-card {
    width: 900px;
    height: 514px;
    background: var(--card-light);
    box-shadow: 0 10px 30px rgba(0,0,0,0.25);
    display: flex;
    flex-direction: column;
    overflow: hidden;
  }
  .service-band {
    background: var(--card-dark);
    height: 226px;
    display: flex;
    flex-direction: column;
    align-items: center;
    justify-content: center;
    text-align: center;
  }
  .brand {
    display: flex;
    align-items: center;
    gap: 12px;
  }
  .brand__dot {
    width: 16px;
    height: 16px;
    border-radius: 50%;
    background: var(--gold);
  }
  .brand__name {
    color: var(--gold);
    font-size: 28px;
    font-weight: 400;
    line-height: 1;
  }
  .service-description {
    margin-top: 16px;
    color: var(--text-light);
    font-size: 19px;
    font-weight: 400;
    line-height: 1.3;
  }
  .identity {
    flex: 1;
    display: flex;
    justify-content: space-between;
    align-items: flex-end;
    padding: 0 40px 56px 48px;
  }
  .person__name {
    color: var(--gold);
    font-size: 30px;
    font-weight: 400;
    margin-bottom: 6px;
  }
  .person__titles {
    list-style: none;
    color: var(--text-dark);
    font-size: 19px;
    line-height: 1.32;
  }
  .contact {
    list-style: none;
    color: var(--text-dark);
    font-size: 19px;
    line-height: 1.35;
    margin-bottom: 18px;
  }
  .contact__item {
    display: flex;
    align-items: center;
    gap: 12px;
  }
  .contact__icon {
    width: 18px;
    height: 18px;
    fill: var(--gold);
    flex-shrink: 0;
  }
</style>
</head>
<body>
<main class="canvas">
  <article class="business-card">
    <section class="service-band">
      <div class="brand">
        <span class="brand__dot"></span>
        <h1 class="brand__name">Fieldstone Mentoring</h1>
      </div>
      <p class="service-description">
        I help founders to start a succesful business with minimum risks and costs.<br>
        I use my 20 years of experience in sales, management and entrepreneurship<br>
        to help them identify the most efficient ways, in terms of time and cost,<br>
        to validate their business idea.
      </p>
    </section>
    <section class="identity">
      <div class="person">
        <h2 class="person__name">Tudor Vasilache</h2>
        <ul class="person__titles">
          <li>Business Angel</li>
          <li>Vocational Mentor</li>
          <li>Learning Designer</li>
        </ul>
      </div>
      <ul class="contact">
        <li class="contact__item">
          <svg class="contact__icon" viewBox="0 0 24 24" aria-hidden="true"><path d="M3 8c0-2 4-4 9-4s9 2 9 4v2h-5V8H8v2H3zM6 11h12l2 8H4z"/></svg>
          +40-745-TUDORV
        </li>
        <li class="contact__item">
          <svg class="contact__icon" viewBox="0 0 24 24" aria-hidden="true"><path d="M2 5h20v14H2zM3.5 6.5 12 13l8.5-6.5z" fill-rule="evenodd"/></svg>
          info@tudorvasilache.example
        </li>
        <li class="contact__item">
          <svg class="contact__icon" viewBox="0 0 24 24" aria-hidden="true"><path d="M12 2a10 10 0 1 0 0 20 10 10 0 0 0 0-20zm0 2c1.3 1.6 2.2 4 2.4 7H9.6C9.8 8 10.7 5.6 12 4zm-2.4 9h4.8c-.2 3-1.1 5.4-2.4 7-1.3-1.6-2.2-4-2.4-7zM4.1 11a8 8 0 0 1 4.4-6.2A14 14 0 0 0 7.6 11zm0 2h3.5c.1 2.3.5 4.4 1.3 6.2A8 8 0 0 1 4.1 13zm12.3 0h3.5a8 8 0 0 1-4.4 6.2c.5-1.8.9-3.9.9-6.2zm0-2c-.1-2.3-.5-4.4-1.3-6.2A8 8 0 0 1 19.9 11z"/></svg>
          www.tudorvasilache.example
        </li>
      </ul>
    </section>
  </article>
</main>
</body>
</html>
```